Lantern Quillhouse Website

Create website for Legal Management Company which specializes in Law Office Spersriinal Management
System implementation & Training
Global presence
Paralegal Services - Remote or In-Office
Legal Research
- Judge Motion Ruling History
- Opposing Counsel Opposition Research - Historical Filings - Pattern identification
Service by Mail - Ex- Parte Notice

Probate -Heir Finder - Asset Location -

```html
<!DOCTYPE html>
<html lang="en">
<head>
<meta charset="utf-8">
<title>Lantern Quillhouse – Legal Management</title>
<link rel="stylesheet" href="https://fonts.googleapis.com/css2?family=Poppins:ital,wght@0,400;0,500;0,600;1,400&display=swap">
<style>
:root{
  --green:#173b2d;
  --green-2:#1f4a38;
  --orange:#d4470f;
  --cream:#fdf0d8;
  --grey:#efefef;
  --ink:#1b1b1b;
  --muted:#555;
  --white:#fff;
}
*{box-sizing:border-box;margin:0;padding:0}
html,body{width:1200px;height:5272px;overflow:hidden}
body{font-family:'Poppins',sans-serif;color:var(--ink);background:var(--white);position:relative}
.abs{position:absolute}
section,header,footer{position:absolute;left:0;width:1200px;overflow:hidden}
.label{color:var(--orange);font-size:14px;font-weight:500;display:flex;align-items:center;gap:8px}
.label::before{content:"";width:6px;height:6px;border-radius:50%;background:var(--orange)}
.btn{display:inline-flex;align-items:center;justify-content:center;gap:8px;font-size:13px;font-weight:500;border-radius:6px}
.btn-orange{background:var(--orange);color:#fff}
.btn-white{background:#fff;color:var(--ink)}
.ph{display:block}

/* nav */
.nav{top:0;height:57px;background:#fff;display:flex;align-items:center}
.logo{font-size:18px;font-weight:400;color:var(--ink);letter-spacing:.2px}
.nav .logo{position:absolute;left:88px}
.nav ul{position:absolute;left:500px;display:flex;gap:32px;list-style:none;font-size:12.5px}
.nav li.active{position:relative}
.nav li.active::after{content:"";position:absolute;left:50%;bottom:-9px;width:4px;height:4px;margin-left:-2px;border-radius:50%;background:var(--orange)}

/* hero */
.hero{top:57px;height:684px;background:linear-gradient(90deg,var(--green) 0%,var(--green) 50%,#2a5544 100%);color:#fff}
.hero h1{position:absolute;left:88px;top:228px;font-size:37px;font-weight:600;line-height:46px}
.hero p{position:absolute;left:90px;top:335px;width:590px;font-size:12.5px;line-height:19px}
.hero .btns{position:absolute;left:90px;top:412px;display:flex;gap:12px}
.hero .btn{height:40px;padding:0 40px}
.hero .arrows{position:absolute;left:90px;top:606px;display:flex;gap:6px}
.circ{width:32px;height:32px;border-radius:50%;display:flex;align-items:center;justify-content:center}
.hero .circ.o{border:1.5px solid #fff}
.hero .circ.f{background:rgba(255,255,255,.25)}
.mouse{position:absolute;left:590px;top:626px;width:18px;height:28px;border:2px solid #fff;border-radius:9px}
.mouse::after{content:"";position:absolute;left:6px;top:5px;width:2px;height:6px;background:#fff;border-radius:1px}

/* about */
.about{top:741px;height:689px;background:var(--cream)}
.about .label{position:absolute;left:90px;top:160px}
.about h2{position:absolute;left:90px;top:190px;font-size:28px;font-weight:600;line-height:36px}
.about .copy{position:absolute;left:90px;top:277px;width:430px;font-size:12.5px;line-height:19px;color:#333}
.about .copy p{margin-bottom:14px}
.about .btn{position:absolute;left:90px;top:473px;width:193px;height:40px}
.about .photo{position:absolute;left:596px;top:119px;width:514px;height:424px;border-radius:12px;background:linear-gradient(160deg,#6d6358 0%,#2b2925 55%,#141414 100%)}

/* services */
.services{top:1430px;height:680px}
.sec-title{text-align:center;font-size:26px;font-weight:500}
.services .sec-title{position:absolute;top:80px;width:100%}
.services .arrows{position:absolute;left:1034px;top:86px;display:flex;gap:6px}
.services .circ.o{border:1.5px solid #333}
.services .circ.f{background:#e4e4e4}
.cards{position:absolute;top:149px;left:90px;display:flex;gap:9px}
.card{width:292px;height:444px;border-radius:12px;background:#fff;box-shadow:0 4px 18px rgba(0,0,0,.08);overflow:hidden}
.card .img{height:240px}
.card h3{font-size:17px;font-weight:500;line-height:22px;margin:28px 30px 6px}
.card p{font-size:12px;line-height:19px;color:var(--muted);margin:0 30px}

/* probate */
.probate{top:2124px;left:90px;width:1020px;height:344px;border:1.5px solid #999;border-radius:22px}
.probate .sec-title{margin-top:74px}
.p-item{position:absolute;top:158px;display:flex;gap:26px}
.icon-sq{width:92px;height:92px;border-radius:6px;background:var(--orange);display:flex;align-items:center;justify-content:center}
.p-item h4{font-size:16px;font-weight:500;margin-top:10px}
.p-item p{font-size:12px;line-height:19px;color:var(--muted);width:210px;margin-top:8px}

/* global */
.global{top:2500px;height:418px}
.global .map{position:absolute;left:123px;top:20px;width:430px;height:380px;border-radius:50%;background:radial-gradient(circle at 45% 50%,#d9d9d9 0%,#ececec 55%,#fff 72%)}
.global .label{position:absolute;left:590px;top:132px}
.global h2{position:absolute;left:590px;top:160px;font-size:26px;font-weight:500}
.global p{position:absolute;left:590px;top:212px;width:440px;font-size:12px;line-height:19px;color:var(--muted)}

/* features */
.features{top:2918px;height:426px;background:var(--grey)}
.features .sec-title{position:absolute;top:97px;width:100%}
.feat{position:absolute;top:174px;width:220px;margin-left:-110px;text-align:center}
.feat .ic{width:92px;height:92px;margin:0 auto;border-radius:4px;background:var(--green);display:flex;align-items:center;justify-content:center}
.feat .ic.alt{background:var(--orange)}
.feat p{font-size:13px;font-weight:500;line-height:20px;margin-top:18px}

/* industries */
.industries{top:3344px;height:520px}
.industries .sec-title{position:absolute;top:84px;width:100%}
.ind{position:absolute;top:146px;width:248px;height:327px;overflow:hidden}
.ind .cap{position:absolute;left:30px;bottom:40px;color:#fff;font-size:11px;font-weight:500;line-height:15px}

/* reviews */
.reviews{top:3900px;height:500px}
.reviews .label{position:absolute;top:28px;left:0;width:100%;justify-content:center}
.reviews .sec-title{position:absolute;top:66px;width:100%;font-size:32px}
.rev{position:absolute;top:150px;width:270px;margin-left:-135px;text-align:center}
.rev .av{width:50px;height:50px;border-radius:50%;margin:0 auto 22px;background:linear-gradient(135deg,#8a6d5a,#3d2e26)}
.rev blockquote{font-size:12px;font-style:italic;line-height:20px;color:#333}
.rev .name{font-size:13px;font-weight:500;margin-top:14px}
.stars{color:#f2a20c;font-size:11px;letter-spacing:1px}

/* contact */
.contact{top:4400px;height:352px;overflow:visible}
.contact h2{position:absolute;left:219px;top:114px;font-size:34px;font-weight:500}
.contact p{position:absolute;left:221px;top:168px;width:300px;font-size:11.5px;line-height:18px;color:#333}
.contact .btn{position:absolute;left:221px;top:244px;width:168px;height:38px;background:#232323;color:#fff;border-radius:20px;font-size:11.5px}
.form{position:absolute;left:602px;top:20px;width:385px;height:352px;border-radius:36px;background:var(--orange);z-index:2}
.field{position:absolute;left:41px;width:303px;height:40px;border-radius:20px;background:rgba(255,255,255,.12);color:#fff;font-size:12px;display:flex;align-items:center;padding-left:28px}
.submit{position:absolute;left:41px;top:288px;width:303px;height:44px;border-radius:22px;background:#fff;color:var(--ink);font-size:13px;font-weight:500;display:flex;align-items:center;justify-content:center;gap:8px}

/* footer */
.footer{top:4752px;height:520px;background:var(--green);color:#fff}
.footer .logo{position:absolute;left:92px;top:222px;color:#fff;font-size:26px}
.fcol{position:absolute;top:168px}
.fcol h5{font-size:15px;font-weight:500;margin-bottom:14px}
.fcol ul{list-style:none;font-size:11px;line-height:31px}
.ci{display:flex;gap:10px;font-size:11px;line-height:16px;margin-bottom:20px}
.ci svg{flex:none;margin-top:2px}
.fcol .sub{font-size:11px;line-height:17px;width:200px}
.newsletter{margin-top:26px;width:259px;height:40px;border-radius:20px;background:rgba(255,255,255,.12);display:flex;align-items:center;padding:0 16px;font-size:11.5px;gap:8px}
.socials{display:flex;gap:8px;margin-top:20px}
.socials span{width:30px;height:30px;border-radius:50%;border:1px solid rgba(255,255,255,.6);display:flex;align-items:center;justify-content:center}
.socials span::after{content:"";width:8px;height:8px;border-radius:50%;background:#fff}
.copy-r{position:absolute;left:0;top:469px;width:100%;text-align:center;font-size:10.5px}
.totop{position:absolute;left:1139px;top:442px;width:42px;height:42px;border-radius:50%;background:var(--orange);display:flex;align-items:center;justify-content:center}
</style>
</head>
<body>

<header class="nav">
  <span class="logo">Lantern Quillhouse</span>
  <ul>
    <li class="active">Home</li><li>About Us</li><li>Services</li><li>Global Presence</li><li>Why Lantern Quillhouse</li><li>Contact Us</li>
  </ul>
</header>

<section class="hero">
  <h1>Smarter Legal Operations.<br>Stronger Case Strategy.</h1>
  <p>Lantern Quillhouse is a legal management company specializing in law office systems, paralegal support, and advanced legal research. We help law firms operate efficiently, make informed decisions, and gain a strategic advantage in every case.</p>
  <div class="btns">
    <span class="btn btn-orange">Get a Consultation</span>
    <span class="btn btn-white">Explore Our Services</span>
  </div>
  <div class="arrows">
    <span class="circ o"><svg width="10" height="10" viewBox="0 0 10 10"><path d="M6 2 3 5l3 3" stroke="#fff" fill="none" stroke-width="1.4"/></svg></span>
    <span class="circ f"><svg width="10" height="10" viewBox="0 0 10 10"><path d="M4 2l3 3-3 3" stroke="#fff" fill="none" stroke-width="1.4"/></svg></span>
  </div>
  <span class="mouse"></span>
</section>

<section class="about">
  <span class="label">About</span>
  <h2>Lantern Quillhouse –<br>Legal Management Experts</h2>
  <div class="copy">
    <p>Lantern Quillhouse is a global legal management company dedicated to optimizing law office operations through specialized system implementation, professional training, and strategic legal support. Our mission is to empower law firms with the tools, insights, and expertise needed to operate efficiently and deliver exceptional results.</p>
    <p>Our mission is to empower law firms with the insights, tools, and expertise necessary to operate seamlessly, make informed decisions, and achieve exceptional results for their clients.</p>
  </div>
  <span class="btn btn-orange">Read More About Us
    <svg width="10" height="10" viewBox="0 0 10 10"><path d="M2 8 8 2M3 2h5v5" stroke="#fff" fill="none" stroke-width="1.3"/></svg></span>
  <div class="photo ph" role="img" aria-label="Portrait of a lawyer in a black robe"></div>
</section>

<section class="services">
  <h2 class="sec-title">Our Services</h2>
  <div class="arrows">
    <span class="circ o"><svg width="10" height="10" viewBox="0 0 10 10"><path d="M6 2 3 5l3 3" stroke="#333" fill="none" stroke-width="1.4"/></svg></span>
    <span class="circ f"><svg width="10" height="10" viewBox="0 0 10 10"><path d="M4 2l3 3-3 3" stroke="#333" fill="none" stroke-width="1.4"/></svg></span>
  </div>
  <div class="cards">
    <article class="card">
      <div class="img ph" role="img" aria-label="Professional working on a laptop in a bright office" style="background:linear-gradient(135deg,#e8e6e2,#6b6660)"></div>
      <h3>Law Office System<br>Setup &amp; Training</h3>
      <p>We implement and optimize law office management systems, ensuring seamless workflows, improved productivity, and proper staff training for long-term success.</p>
    </article>
    <article class="card">
      <div class="img ph" role="img" aria-label="Paralegal reviewing documents at a desk" style="background:linear-gradient(135deg,#8e7a66,#3a3028)"></div>
      <h3>Paralegal Support<br>(Remote &amp; On-Site)</h3>
      <p>Flexible paralegal support tailored to your firm’s needs, available remotely or on-site to assist with case preparation, documentation, and filings.</p>
    </article>
    <article class="card">
      <div class="img ph" role="img" aria-label="Gavel resting on law books" style="background:linear-gradient(135deg,#9a5a32,#3a1d10)"></div>
      <h3>Legal Research<br>&amp; Analysis</h3>
      <p>In-depth legal research including statutes, case law, precedents, and jurisdiction-specific analysis to support strong legal arguments.</p>
    </article>
    <article class="card">
      <div class="img ph" role="img" aria-label="Columned courthouse building under a blue sky" style="background:linear-gradient(180deg,#4f7fb8,#c9c2b3)"></div>
      <h3>Judge Ruling<br>History Analysis</h3>
      <p>Comprehensive analysis of judges’ past rulings and motion outcomes to help shape effective litigation strategies.</p>
    </article>
  </div>
</section>

<section class="probate">
  <h2 class="sec-title">Probate Services</h2>
  <div class="p-item" style="left:136px">
    <span class="icon-sq"><svg width="46" height="46" viewBox="0 0 46 46" fill="none" stroke="#fff" stroke-width="2"><circle cx="17" cy="20" r="10"/><circle cx="17" cy="20" r="4"/><path d="M10 34h14M30 12h10v24H30z"/></svg></span>
    <div><h4>Heir Finder</h4><p>Locating rightful heirs efficiently and accurately.</p></div>
  </div>
  <div class="p-item" style="left:544px">
    <span class="icon-sq"><svg width="46" height="46" viewBox="0 0 46 46" fill="none" stroke="#fff" stroke-width="2"><path d="M6 36 12 18h26l-4 18z"/><circle cx="31" cy="14" r="6"/><path d="M31 20v6M15 28h10"/></svg></span>
    <div><h4>Asset Location</h4><p>Identifying and tracing assets for probate and estate matters.</p></div>
  </div>
</section>

<section class="global">
  <div class="map ph" role="img" aria-label="Dotted world globe with office locations marked"></div>
  <span class="label">Global Presence</span>
  <h2>Serving Law Firms Worldwide</h2>
  <p>Lantern Quillhouse supports law firms across multiple countries. Our global reach allows us to deliver consistent, high-quality legal management and research services regardless of location.</p>
</section>

<section class="features">
  <h2 class="sec-title">Deep understanding of legal workflows</h2>
  <div class="feat" style="left:209px"><span class="ic"><svg width="40" height="40" viewBox="0 0 40 40" fill="none" stroke="#fff" stroke-width="1.8"><path d="M20 6v28M10 34h20M8 12h24M8 12l-4 10h8zM32 12l-4 10h8z"/></svg></span><p>Deep understanding of<br>legal workflows</p></div>
  <div class="feat" style="left:420px"><span class="ic"><svg width="40" height="40" viewBox="0 0 40 40" fill="none" stroke="#fff" stroke-width="1.8"><path d="M10 4h14l6 6v26H10z"/><path d="M15 18h10M15 24h10M15 30h6"/></svg></span><p>Experienced legal and<br>research professionals</p></div>
  <div class="feat" style="left:596px"><span class="ic alt"><svg width="40" height="40" viewBox="0 0 40 40" fill="none" stroke="#fff" stroke-width="1.8"><circle cx="20" cy="20" r="8"/><path d="M20 4v6M20 30v6M4 20h6M30 20h6M9 9l4 4M27 27l4 4M31 9l-4 4M9 31l4-4"/></svg></span><p>Technology-driven<br>solutions</p></div>
  <div class="feat" style="left:770px"><span class="ic"><svg width="40" height="40" viewBox="0 0 40 40" fill="none" stroke="#fff" stroke-width="1.8"><circle cx="20" cy="20" r="13"/><circle cx="20" cy="20" r="6"/><path d="M20 7v7M20 26v7M7 20h7M26 20h7"/></svg></span><p>Scalable support for<br>firms of all sizes</p></div>
  <div class="feat" style="left:975px"><span class="ic"><svg width="40" height="40" viewBox="0 0 40 40" fill="none" stroke="#fff" stroke-width="1.8"><path d="M20 5 32 10v9c0 8-5 13-12 16-7-3-12-8-12-16v-9z"/><path d="m15 20 4 4 7-8"/></svg></span><p>Confidential, accurate, and<br>reliable services</p></div>
</section>

<section class="industries">
  <h2 class="sec-title">Industries We Serve</h2>
  <div class="ind" style="left:90px;background:linear-gradient(180deg,#d8d4cc 0%,#8a8276 55%,#1f3a2d 100%)" role="img" aria-label="Smiling lawyer shaking hands with a client"><span class="cap">Law Firms &amp;<br>Legal Practices</span></div>
  <div class="ind" style="left:348px;background:linear-gradient(180deg,#8a7460 0%,#4a3a2c 55%,#1f3a2d 100%)" role="img" aria-label="Gavel in front of an attorney"><span class="cap">Litigation &amp;<br>Trial Attorneys</span></div>
  <div class="ind" style="left:606px;background:linear-gradient(180deg,#3d4a5a 0%,#6d5a48 55%,#1f3a2d 100%)" role="img" aria-label="Attorney signing papers beside scales and a model house"><span class="cap">Probate &amp; Estate<br>Law Firms</span></div>
  <div class="ind" style="left:864px;background:linear-gradient(180deg,#3a4e5a 0%,#566a70 55%,#1f3a2d 100%)" role="img" aria-label="Business professionals reviewing documents"><span class="cap">Corporate Legal<br>Departments</span></div>
</section>

<section class="reviews">
  <span class="label">Clients Review</span>
  <h2 class="sec-title">Trusted by 15,000+happy customers</h2>
  <div class="rev" style="left:264px"><div class="av ph" role="img" aria-label="Client avatar"></div><blockquote>It is a long established fact that a reader will be distracted by the readable content of a page when looking at its layout. The point of using Lorem Ipsum is that it has a more-or-less normal distribution of letters, as opposed to using 'Content here,</blockquote><p class="name">Mara Ellison</p><p class="stars">★★★★★</p></div>
  <div class="rev" style="left:600px"><div class="av ph" role="img" aria-label="Client avatar"></div><blockquote>It is a long established fact that a reader will be distracted by the readable content of a page when looking at its layout. The point of using Lorem Ipsum is that it has a more-or-less normal distribution of letters, as opposed to using 'Content here,</blockquote><p class="name">Mara Ellison</p><p class="stars">★★★★★</p></div>
  <div class="rev" style="left:936px"><div class="av ph" role="img" aria-label="Client avatar"></div><blockquote>It is a long established fact that a reader will be distracted by the readable content of a page when looking at its layout. The point of using Lorem Ipsum is that it has a more-or-less normal distribution of letters, as opposed to using 'Content here,</blockquote><p class="name">Mara Ellison</p><p class="stars">★★★★★</p></div>
</section>

<section class="contact">
  <h2>Get in Touch</h2>
  <p>Connect with our experts to discuss your legal management needs, schedule a consultation, or request a tailored service package.</p>
  <span class="btn">Get a Free Quote <svg width="10" height="10" viewBox="0 0 10 10"><path d="M2 8 8 2M3 2h5v5" stroke="#fff" fill="none" stroke-width="1.3"/></svg></span>
  <div class="form">
    <span class="field" style="top:49px">Name</span>
    <span class="field" style="top:103px">Email</span>
    <span class="field" style="top:158px">Company / Law Firm</span>
    <span class="field" style="top:211px">Message</span>
    <span class="submit">Submit Inquiry <svg width="10" height="10" viewBox="0 0 10 10"><path d="M2 8 8 2M3 2h5v5" stroke="#1b1b1b" fill="none" stroke-width="1.3"/></svg></span>
  </div>
</section>

<footer class="footer">
  <span class="logo">Lantern Quillhouse</span>
  <div class="fcol" style="left:407px">
    <h5>Quick Links</h5>
    <ul><li>Home</li><li>About Us</li><li>Services</li><li>Global Presence</li><li>Insights / Research</li><li>Contact</li></ul>
  </div>
  <div class="fcol" style="left:592px">
    <h5>Contact Info</h5>
    <div class="ci"><svg width="12" height="12" viewBox="0 0 12 12"><rect x="1" y="2.5" width="10" height="7" fill="none" stroke="#e05a22" stroke-width="1.3"/><path d="m1 3 5 4 5-4" fill="none" stroke="#e05a22" stroke-width="1.3"/></svg><span>Email:<br>info@lanternquillhouse.com</span></div>
    <div class="ci"><svg width="12" height="12" viewBox="0 0 12 12"><path d="M2 1.5h2.5l1 2.5-1.5 1a7 7 0 0 0 3 3l1-1.5 2.5 1V10A1 1 0 0 1 9.5 11 8.5 8.5 0 0 1 1 2.5 1 1 0 0 1 2 1.5z" fill="#e05a22"/></svg><span>Phone:<br>+XX XXX XXX XXXX</span></div>
    <div class="ci"><svg width="12" height="12" viewBox="0 0 12 12"><path d="M6 11S2 7 2 4.5a4 4 0 0 1 8 0C10 7 6 11 6 11z" fill="none" stroke="#e05a22" stroke-width="1.3"/><circle cx="6" cy="4.5" r="1.3" fill="#e05a22"/></svg><span>Location:<br>123 Main Street,<br>[Your City, State ZIP]</span></div>
  </div>
  <div class="fcol" style="left:854px">
    <h5>Newsletter</h5>
    <p class="sub">Subscribe to our email address to get the latest news.</p>
    <div class="newsletter"><svg width="12" height="12" viewBox="0 0 12 12"><rect x="1" y="2.5" width="10" height="7" fill="none" stroke="#e05a22" stroke-width="1.3"/><path d="m1 3 5 4 5-4" fill="none" stroke="#e05a22" stroke-width="1.3"/></svg><span style="flex:1">Enter your email...</span><svg width="14" height="14" viewBox="0 0 14 14"><path d="M1 7 13 1 9 13 7 8z" fill="#e05a22"/></svg></div>
    <div class="socials"><span></span><span></span><span></span><span></span></div>
  </div>
  <p class="copy-r">© Copyright 2025 Lantern Quillhouse. All Rights Reserved.</p>
  <span class="totop"><svg width="14" height="14" viewBox="0 0 14 14"><path d="M7 12V2M3 6l4-4 4 4" stroke="#fff" fill="none" stroke-width="1.6"/></svg></span>
</footer>

</body>
</html>
```